Standee design for an exhibition event

"Please read the details carefully:

80 cm (W) X 200 cm (H)
Res: 150dpi
output file : ai file.
Corporate Health Checkups
- Companies understand the importance of executive wellness for their employees. An unfit and unhealthy employee loses his productivity due to frequent absenteeism, lack of concentration and low energy levels at work. Regular health screening is the key to good employee health management.

```html
<!DOCTYPE html>
<html lang="en">
<head>
<meta charset="UTF-8">
<title>Corporate Health Checkups – Standee</title>
<link href="https://fonts.googleapis.com/css2?family=Montserrat:wght@300;400;500;600;700&display=swap" rel="stylesheet">
<style>
  :root {
    --paper: #ffffff;
    --mist: #e7e7e7;
    --brand-green: #2a7d62;
    --footer-green: #2b7a60;
    --slate: #6e6e6e;
    --ink: #1d1d1d;
    --body-grey: #4a4a4a;
    --accent-pink: #e8265a;
    --accent-blue: #3bb8d8;
    --dot-grey: #d5d5d5;
  }
  * { margin: 0; padding: 0; box-sizing: border-box; }
  html, body { width: 1200px; height: 3000px; overflow: hidden; }
  body { font-family: "Montserrat", sans-serif; background: var(--paper); }
  .standee { position: relative; width: 1200px; height: 3000px; background: var(--paper); overflow: hidden; }

  .header-band { position: absolute; left: 0; top: 0; width: 1200px; height: 420px; background: var(--mist); }
  .brand { position: absolute; left: 0; top: 82px; width: 1200px; text-align: center; }
  .brand-name { font-weight: 700; font-size: 96px; letter-spacing: -2px; color: var(--brand-green); line-height: 1; }

  .hero-art { position: absolute; left: 0; top: 0; }

  .hero-title { position: absolute; left: 94px; top: 1066px; color: #fff; font-weight: 700; font-size: 78px; line-height: 96px; }
  .hero-title .dot { display: inline-block; width: 16px; height: 16px; border-radius: 50%; background: var(--accent-pink); margin: 0 2px; vertical-align: 2px; }
  .hero-underline { position: absolute; left: 94px; top: 1268px; width: 526px; height: 6px; background: var(--accent-pink); }

  .intro { position: absolute; left: 94px; top: 1552px; width: 956px; color: var(--ink); }
  .intro-kicker { font-weight: 500; font-size: 30px; letter-spacing: .5px; }
  .intro-text { margin-top: 12px; font-weight: 400; font-size: 34px; line-height: 46px; text-align: justify; }
  .intro-sign { margin-top: 6px; font-weight: 500; font-size: 30px; }

  .about-row { position: absolute; left: 94px; top: 1820px; width: 580px; height: 76px; }
  .about-button { position: absolute; left: 0; top: 0; width: 382px; height: 76px; border: 2px solid #aaa; border-radius: 18px; display: flex; align-items: center; justify-content: center; font-weight: 600; font-size: 38px; color: var(--ink); letter-spacing: 1px; }
  .about-line { position: absolute; left: 382px; top: 37px; width: 180px; height: 2px; background: #aaa; }
  .about-dot { position: absolute; left: 554px; top: 27px; width: 24px; height: 24px; border-radius: 50%; background: var(--accent-pink); }

  .section-heading { position: absolute; left: 0; top: 1958px; width: 1200px; text-align: center; font-weight: 700; font-size: 58px; line-height: 76px; color: var(--slate); letter-spacing: 1px; }
  .section-dots { position: absolute; top: 2056px; left: 954px; display: flex; gap: 22px; }
  .section-dots span { width: 22px; height: 22px; border-radius: 50%; }
  .section-dots .blue { background: var(--accent-blue); }
  .section-dots .grey { background: var(--dot-grey); }

  .section-body { position: absolute; left: 94px; top: 2162px; width: 986px; font-weight: 300; font-size: 47px; line-height: 62px; letter-spacing: 0.4px; color: var(--body-grey); text-align: justify; }

  .footer-art { position: absolute; left: 0; top: 2700px; }
  .footer-info { position: absolute; top: 2852px; color: #fff; font-weight: 600; font-size: 32px; line-height: 52px; }
  .footer-info.left { left: 94px; }
  .footer-info.right { right: 120px; font-weight: 500; }
</style>
</head>
<body>
<main class="standee">
  <div class="header-band"></div>
  <div class="brand">
    <div class="brand-name">Meridian Hospital</div>
  </div>

  <svg class="hero-art" width="1200" height="1460" viewBox="0 0 1200 1460" role="img" aria-label="Photo of a smiling patient greeting a doctor in a clinic, tinted teal">
    <defs>
      <linearGradient id="heroTint" x1="0" y1="0" x2="1" y2="1">
        <stop offset="0" stop-color="#4fc9c9"/>
        <stop offset=".55" stop-color="#28b2b6"/>
        <stop offset="1" stop-color="#7ed3cf"/>
      </linearGradient>
    </defs>
    <path d="M560 1400 C 760 1330 960 1320 1200 1330 L1200 1440 C 1000 1450 760 1440 560 1400 Z" fill="#6c6c6c"/>
    <path d="M0 350 C 300 290 800 280 1200 360 L1200 1330 C 980 1310 800 1330 620 1390 C 420 1450 200 1440 0 1370 Z" fill="url(#heroTint)"/>
    <path d="M0 1370 C 200 1440 420 1450 620 1390" fill="none" stroke="#1a8e96" stroke-width="4"/>
  </svg>

  <h1 class="hero-title">Corporate<br>Health<span class="dot"></span>Checkups</h1>
  <div class="hero-underline"></div>

  <section class="intro">
    <p class="intro-kicker">WE ARE JUST GETTING STARTED</p>
    <p class="intro-text">Lorem ipsum dolor sit amet, ut qui vidit lucilius, te iisque maiorum eligendi sit. Cum et alii harum facete. Ut sed atqui doming posidonium.</p>
    <p class="intro-sign">JOHN DOE | DIRECTOR</p>
  </section>

  <div class="about-row">
    <div class="about-button">ABOUT</div>
    <div class="about-line"></div>
    <div class="about-dot"></div>
  </div>

  <h2 class="section-heading">CORPORATE<br>HEALTH CHECKUPS</h2>
  <div class="section-dots"><span class="blue"></span><span class="grey"></span></div>

  <p class="section-body">Companies understand the importance of executive wellness for their employees. An unfit and unhealthy employee loses his productivity due to frequent absenteeism, lack of concentration and low energy levels at work. Regular health screening is the key to good employee health management.</p>

  <svg class="footer-art" width="1200" height="300" viewBox="0 0 1200 300">
    <path d="M0 30 Q 600 120 1200 30 L1200 300 L0 300 Z" fill="var(--footer-green)"/>
  </svg>
  <div class="footer-info left">Main Street | Local Building<br>+ (012) 345 678 901</div>
  <div class="footer-info right">www.website.com<br>contact@mail.com</div>
</main>
</body>
</html>
```